American alt-rock band needs eye-catching album cover for new record

We need an album cover for our new cd. The band is called Amber Lantern, the music is alt-rock, an interesting mix of styles and infuences- Elements of The Vanes, K7, Dan Hollis, Walt Brice The Farrows and Carl Whitmoreland are all evident in the sound. Classic rock with atmospheric elements and sweeping melodies. The album is titled "Nothing Stays Where You Left It". We are interested in designs that focus on a single direct subject and are not too busy in nature. Visually striking, yet simple and memorable. Stark contrasts between dark and light. Album covers such as Lumen Drift's "Harbinger", Gray Orchid's "Quiet Edge of The Tide" and Opal Ferry's self titled release are along the lines of what we were hoping for. An idea we had included an image of a man looking at two doors, or two paths, something involving the imagery of decisions (a door number one or number two type concept). Also like simple designs maybe with the subject in a lower corner of the image (this doesn't have to followed if it makes more sense for the image to be centered though). Solid color backgrounds. Colors we like include black, white,deep reds/blues/purples. Not all of them need to be included, but could be (white/black, white/purple, black/red, etc) Please include the band name and album name within the design.

Target Market(s)

18-39

Colors
6b449b
ec1f27
000000
474747
fbfbfb

Requirements
Must have
• Band name and album title must be included in design
Nice to have
• Would like to see something "dream-like" but not too much outer space/sci-fi imagery. Would like to see the moon motel image that I have added used in some way.
Should not have
• no skulls or heavy metal imagery. Dark is ok, but in a more artistic way.

```html
<!DOCTYPE html>
<html lang="en">
<head>
<meta charset="utf-8">
<title>Amber Lantern — Nothing Stays Where You Left It</title>
<link href="https://fonts.googleapis.com/css2?family=Open+Sans:ital,wght@0,600;1,400;1,700&display=swap" rel="stylesheet">
<style>
  :root {
    --paper: #ffffff;
    --ink: #000000;
    --charcoal: #333234;
    --slate: #67646a;
    --violet: #6b449b;
    --violet-deep: #3a2257;
    --stroke-grey: #6f6a66;
  }
  html, body {
    margin: 0;
    padding: 0;
    overflow: hidden;
    background: var(--paper);
  }
  .album-cover {
    position: relative;
    width: 1200px;
    height: 1200px;
    background: var(--paper);
    overflow: hidden;
    font-family: "Open Sans", Arial, sans-serif;
  }
  .cover-art {
    position: absolute;
    left: 30px;
    top: 60px;
    width: 1080px;
    height: 1000px;
    z-index: 1;
    background:
      radial-gradient(ellipse 48% 46% at 42% 52%, var(--violet) 0%, rgba(107, 68, 155, 0.85) 45%, rgba(58, 34, 87, 0.35) 70%, rgba(111, 106, 102, 0.15) 85%, rgba(255, 255, 255, 0) 100%);
  }
  .band-name {
    position: absolute;
    right: 4px;
    top: 98px;
    margin: 0;
    z-index: 2;
    text-align: right;
    line-height: 1;
  }
  .band-name__first {
    display: block;
    font-weight: 600;
    font-size: 156px;
    letter-spacing: -1px;
    color: var(--charcoal);
  }
  .band-name__second {
    display: block;
    margin-top: -28px;
    font-weight: 600;
    font-size: 82px;
    color: var(--slate);
  }
  .album-title {
    position: absolute;
    right: 76px;
    top: 1046px;
    margin: 0;
    z-index: 2;
    text-align: right;
    font-style: italic;
    font-size: 64px;
    line-height: 1;
    color: var(--ink);
    text-transform: uppercase;
  }
  .album-title__lead {
    display: block;
    font-weight: 700;
    letter-spacing: -1px;
  }
  .album-title__tail {
    display: block;
    margin-top: -6px;
    font-weight: 400;
    letter-spacing: -1px;
  }
</style>
</head>
<body>
  <main class="album-cover">
    <div class="cover-art" role="img" aria-label="Painted star of brushed purple triangles layered over a grey hand-drawn star outline"></div>
    <h1 class="band-name">
      <span class="band-name__first">Amber</span>
      <span class="band-name__second">Lantern</span>
    </h1>
    <h2 class="album-title">
      <span class="album-title__lead">Nothing Stays Where</span>
      <span class="album-title__tail">You Left It</span>
    </h2>
  </main>
</body>
</html>
```